We require a Squarespace web design for Mossfield Cannabis Website.
We are an urban community retail cannabis store. We have turn tables set up playing old hip hop/house music to create a lounge vibe. The store is very urban, dark and sexy. We have a couple of concepts that we like. One is a dark stone background and smoke rising up. Such as the link here. https://dev.lumo.varnell.quixo.com/products/
The other is using the black and white map of our community.
We would like to have any concept include the logo on the turntable with the logo spinning like a record and the words MOSSFIELD CANNABIS also spinning around it (such as in the attached giff.)
We tend to gravitate toward black and white and gold for the colours.
5817 Harwick Boulevard West,
Scarborough, ON M4R 7K2
(416) 738-LEAF
Hours of Operation
Open Daily 10:00 - 10:00

```html
<!DOCTYPE html>
<html lang="en">
<head>
<meta charset="utf-8">
<title>Mossfield Cannabis</title>
<link href="https://fonts.googleapis.com/css2?family=Bebas+Neue&family=Roboto:wght@300;400;500;700&display=swap" rel="stylesheet">
<style>
:root{
  --ink:#0b0b0c;
  --header:#17181c;
  --gold:#d9b96a;
  --gold-deep:#b8973f;
  --white:#ffffff;
  --red:#c8343a;
  --muted:#cfcfcf;
  --line:#3a3a3a;
  --display:"Bebas Neue", Impact, sans-serif;
  --body:"Roboto", Arial, sans-serif;
}
*{box-sizing:border-box;margin:0;padding:0}
html,body{width:1200px;height:2791px;overflow:hidden;background:var(--ink);font-family:var(--body);color:var(--white)}
.page{position:relative;width:1200px;height:2791px}
.abs{position:absolute}

/* header */
.site-header{left:0;top:0;width:1200px;height:100px;background:var(--header)}
.brand{left:100px;top:12px;height:76px;display:flex;align-items:center;gap:16px}
.brand-mark{width:74px;height:74px;border-radius:50%;border:3px solid var(--gold)}
.brand-name{font-family:var(--body);font-weight:500;color:var(--gold);font-size:22px;letter-spacing:5px;line-height:1.15;width:200px}
.main-nav{right:102px;top:40px;display:flex;gap:66px}
.main-nav a{color:var(--white);text-decoration:none;font-size:15px;font-weight:500;letter-spacing:.2px}

/* hero */
.hero{left:0;top:100px;width:1200px;height:673px;overflow:hidden;
  background:radial-gradient(ellipse 360px 420px at 860px 300px,#6e8a2c 0%,#3e5420 40%,rgba(20,26,18,0) 75%),
             radial-gradient(ellipse 300px 260px at 600px 560px,#4e5a2c 0%,rgba(20,20,20,0) 70%),
             linear-gradient(90deg,#0d0e12 0%,#15171a 40%,#1b1f18 100%)}
.hero-ring{left:42px;top:68px;width:460px;height:460px;border-radius:50%;border:22px solid rgba(255,255,255,.06)}
.hero-copy{left:60px;top:236px;width:500px;text-align:center}
.hero-title{font-family:var(--display);font-size:54px;line-height:50px;color:var(--white);letter-spacing:.5px}
.hero-title .gold{display:block;color:var(--gold);font-size:58px;line-height:56px}
.hero-sub{font-size:26px;font-weight:300;margin-top:12px;letter-spacing:-.3px}
.btn{display:inline-flex;align-items:center;justify-content:center;gap:6px;font-family:var(--body);font-weight:700;font-size:15px;text-decoration:none;text-transform:uppercase;letter-spacing:-.2px}
.btn-light{background:var(--white);color:var(--ink);width:166px;height:48px;margin-top:22px}
.btn-outline{border:1.5px solid var(--ink);color:var(--ink);height:47px;background:var(--white)}
.hero-prev{left:58px;top:392px}
.dots{left:558px;top:727px;display:flex;gap:12px}
.dots span{width:12px;height:12px;border-radius:50%;border:1.5px solid var(--white)}
.dots span.on{background:var(--white)}

/* promo + categories band */
.stone{left:0;top:773px;width:1200px;height:1446px;
  background:radial-gradient(ellipse 300px 200px at 60px 80px,#4a4a4a 0%,rgba(0,0,0,0) 70%),
             radial-gradient(ellipse 320px 220px at 1150px 110px,#5a5a5a 0%,rgba(0,0,0,0) 70%),
             radial-gradient(ellipse 380px 260px at 60px 1420px,#4d4d4d 0%,rgba(0,0,0,0) 70%),
             radial-gradient(ellipse 380px 260px at 1120px 1420px,#555 0%,rgba(0,0,0,0) 70%),
             linear-gradient(180deg,#1d1d1d 0%,#0a0a0a 30%,#080808 75%,#1c1c1c 100%)}
.promo{top:883px;width:483px;height:352px;background:var(--white);border-radius:4px;overflow:hidden;color:var(--ink)}
.promo-sale{left:103px}
.promo-new{left:614px}
.promo-art{position:absolute}
.promo-sale .promo-art{right:0;bottom:0;width:230px;height:240px;background:radial-gradient(ellipse at 60% 65%,#6f8a2a 0%,#b5a54a 40%,rgba(255,255,255,0) 72%)}
.promo-new .promo-art{right:0;top:0;width:190px;height:230px;background:radial-gradient(ellipse at 55% 45%,#707a52 0%,#a6ab86 40%,rgba(255,255,255,0) 72%)}
.promo-head{position:absolute;left:28px;font-family:var(--display);color:var(--ink)}
.promo-sale .l1{top:44px;font-size:60px;line-height:60px}
.promo-sale .l2{top:114px;font-size:64px;line-height:64px}
.promo-sale .l3{top:190px;font-size:48px;line-height:48px}
.promo-new .promo-head{left:29px;top:50px;font-size:56px;line-height:62px}
.red{color:var(--red)}
.promo .btn{position:absolute;left:29px;top:266px}
.promo-sale .btn{width:181px}
.promo-new .btn{width:166px}

.section-title{left:0;top:1346px;width:1200px;text-align:center;font-family:var(--display);font-size:54px;line-height:58px;color:var(--gold)}
.title-rule{left:577px;top:1415px;width:46px;height:2px;background:var(--white)}

.categories{left:100px;top:1450px;width:1000px;display:grid;grid-template-columns:repeat(4,241px);column-gap:12px;row-gap:62px}
.cat{text-decoration:none;color:var(--white);text-align:center}
.cat-photo{height:249px;background:var(--white)}
.cat-label{margin-top:14px;font-size:20px;font-weight:500;letter-spacing:-.2px}
.ph-flower{background:radial-gradient(ellipse 90px 55px at 50% 48%,#8a7a3a 0%,#b49a5c 50%,#fff 100%)}
.ph-preroll{background:radial-gradient(ellipse 110px 40px at 50% 46%,#b4a288 0%,#e2d9c8 55%,#fff 100%)}
.ph-vape{background:radial-gradient(ellipse 30px 95px at 47% 45%,#8d9095 0%,#d8dadc 60%,#fff 100%)}
.ph-edible{background:radial-gradient(ellipse 90px 50px at 52% 50%,#e59a2a 0%,#f3d27a 50%,#fff 100%)}
.ph-oil{background:radial-gradient(ellipse 45px 95px at 48% 48%,#d7b63a 0%,#efe1a0 55%,#fff 100%)}
.ph-shatter{background:radial-gradient(ellipse 95px 75px at 50% 48%,#e0b53a 0%,#f1da8c 55%,#fff 100%)}
.ph-cbd{background:radial-gradient(ellipse 38px 95px at 48% 50%,#5a4a7c 0%,#9a8fb4 55%,#fff 100%)}
.ph-acc{background:radial-gradient(ellipse 40px 95px at 50% 50%,#e58a3a 0%,#d2e08a 55%,#fff 100%)}

/* footer */
.site-footer{left:0;top:2219px;width:1200px;height:572px;background:radial-gradient(ellipse 300px 260px at 600px 80px,#1f1f1f 0%,rgba(0,0,0,0) 70%),linear-gradient(180deg,#0e0e0e,#161616)}
.mail-title{left:0;top:2303px;width:1200px;text-align:center;font-family:var(--display);font-size:46px;line-height:46px;color:var(--gold)}
.mail-sub{left:0;top:2354px;width:1200px;text-align:center;font-size:16px;font-weight:400}
.signup{left:303px;top:2397px;display:flex;gap:11px}
.email-field{width:427px;height:46px;background:var(--white);display:flex;align-items:center;justify-content:space-between;padding:0 20px 0 22px;color:#555;font-size:12.5px}
.btn-subscribe{width:156px;height:46px;background:var(--white);color:var(--ink)}
.rule{left:100px;width:999px;height:1px;background:var(--line)}
.socials{left:157px;top:2568px;display:flex;gap:9px}
.socials span{width:45px;height:45px;border-radius:50%;background:var(--white)}
.footer-brand{left:440px;top:2545px;display:flex;align-items:center;gap:18px}
.footer-brand .brand-mark{width:92px;height:92px}
.footer-brand .brand-name{font-size:27px;width:230px;letter-spacing:6px}
.contact{left:922px;top:2538px;width:240px;font-size:13px;line-height:24px}
.contact h4{font-size:14px;font-weight:700;margin-bottom:6px;letter-spacing:.2px}
.contact-row{display:flex;gap:8px;margin-bottom:6px;align-items:flex-start}
.contact-row svg{flex:none;margin-top:6px}
.copyright{left:0;top:2746px;width:1200px;text-align:center;font-size:13px}
.to-top{left:1130px;top:2724px;width:44px;height:44px;border-radius:50%;background:var(--white);display:flex;align-items:center;justify-content:center}
</style>
</head>
<body>
<div class="page">

  <header class="site-header abs">
    <a class="brand abs" href="#">
      <span class="brand-mark"></span>
      <span class="brand-name">MOSSFIELD CANNABIS</span>
    </a>
    <nav class="main-nav abs">
      <a href="#">HOME</a>
      <a href="#">CATEGORIES</a>
      <a href="#">REACH US</a>
    </nav>
  </header>

  <section class="hero abs" role="img" aria-label="Close-up photograph of a flowering cannabis plant on a dark background">
    <div class="hero-ring abs"></div>
    <svg class="hero-prev abs" width="24" height="42" viewBox="0 0 24 42" aria-hidden="true"><path d="M21 2 3 21l18 19" fill="none" stroke="#fff" stroke-width="2"/></svg>
    <div class="hero-copy abs">
      <h1 class="hero-title">WELCOME TO <span class="gold">MOSSFIELD CANNABIS</span></h1>
      <p class="hero-sub">Proudly Local and Family Owned</p>
      <a class="btn btn-light" href="#">SHOP ONLINE
        <svg width="15" height="15" viewBox="0 0 16 16" aria-hidden="true"><circle cx="8" cy="8" r="8" fill="#0b0b0c"/><path d="M4 8h6M7.5 5 10.5 8l-3 3" fill="none" stroke="#fff" stroke-width="2"/></svg>
      </a>
    </div>
    <div class="dots abs"><span></span><span class="on"></span><span></span><span></span></div>
  </section>

  <div class="stone abs" role="img" aria-label="Dark stone texture with smoke rising from the edges"></div>

  <article class="promo promo-sale abs">
    <div class="promo-art" role="img" aria-label="Cannabis leaf with a stack of rolled pre-rolls"></div>
    <h2 class="promo-head l1">GRAND OPENING</h2>
    <p class="promo-head l2"><span class="red">10%</span> OFF</p>
    <p class="promo-head l3">ORDERS OVER $35</p>
    <a class="btn btn-outline" href="#">WHAT'S ON SALE
      <svg width="15" height="15" viewBox="0 0 16 16" aria-hidden="true"><circle cx="8" cy="8" r="8" fill="#0b0b0c"/><path d="M4 8h6M7.5 5 10.5 8l-3 3" fill="none" stroke="#fff" stroke-width="2"/></svg>
    </a>
  </article>

  <article class="promo promo-new abs">
    <div class="promo-art" role="img" aria-label="Dried cannabis buds hanging on stems"></div>
    <h2 class="promo-head">NEW ARRIVALS<br>SEE WHAT'S<br><span class="red">HOT !</span></h2>
    <a class="btn btn-outline" href="#">WHAT'S NEW
      <svg width="15" height="15" viewBox="0 0 16 16" aria-hidden="true"><circle cx="8" cy="8" r="8" fill="#0b0b0c"/><path d="M4 8h6M7.5 5 10.5 8l-3 3" fill="none" stroke="#fff" stroke-width="2"/></svg>
    </a>
  </article>

  <h2 class="section-title abs">SHOP BY CATEGORIES</h2>
  <div class="title-rule abs"></div>

  <div class="categories abs">
    <a class="cat" href="#"><div class="cat-photo ph-flower" role="img" aria-label="Dried cannabis flower bud"></div><div class="cat-label">FLOWER</div></a>
    <a class="cat" href="#"><div class="cat-photo ph-preroll" role="img" aria-label="Two crossed pre-rolled joints"></div><div class="cat-label">PRE-ROLLS</div></a>
    <a class="cat" href="#"><div class="cat-photo ph-vape" role="img" aria-label="Silver vaporizer device"></div><div class="cat-label">VAPORIZERS</div></a>
    <a class="cat" href="#"><div class="cat-photo ph-edible" role="img" aria-label="Gummy candies with a cannabis leaf"></div><div class="cat-label">EDIBLES</div></a>
    <a class="cat" href="#"><div class="cat-photo ph-oil" role="img" aria-label="Dropper bottle of golden oil on leaves"></div><div class="cat-label">HIGH THC</div></a>
    <a class="cat" href="#"><div class="cat-photo ph-shatter" role="img" aria-label="Amber shatter concentrate"></div><div class="cat-label">CONCENTRATES</div></a>
    <a class="cat" href="#"><div class="cat-photo ph-cbd" role="img" aria-label="Dropper bottle of CBD oil"></div><div class="cat-label">CBD</div></a>
    <a class="cat" href="#"><div class="cat-photo ph-acc" role="img" aria-label="Small glass water pipe"></div><div class="cat-label">ACCESSORIES</div></a>
  </div>

  <footer class="site-footer abs" role="img" aria-label="Dark background with faint cannabis leaves"></footer>

  <h2 class="mail-title abs">JOIN OUR MAILING LIST</h2>
  <p class="mail-sub abs">Sign Up for News, Events &amp; Much More!</p>
  <form class="signup abs">
    <label class="email-field">Enter your email address...
      <svg width="18" height="13" viewBox="0 0 18 13" aria-hidden="true"><rect x=".75" y=".75" width="16.5" height="11.5" fill="none" stroke="#777" stroke-width="1.2"/><path d="M1 1l8 6 8-6M1 12l6-5M17 12l-6-5" fill="none" stroke="#777" stroke-width="1.2"/></svg>
    </label>
    <span class="btn btn-subscribe">SUBSCRIBE</span>
  </form>

  <div class="rule abs" style="top:2491px"></div>

  <div class="socials abs" aria-label="Social links"><span></span><span></span><span></span><span></span></div>

  <div class="footer-brand abs">
    <span class="brand-mark"></span>
    <span class="brand-name">MOSSFIELD CANNABIS</span>
  </div>

  <address class="contact abs" style="font-style:normal">
    <h4>CONTACT INFO</h4>
    <div class="contact-row">
      <svg width="10" height="13" viewBox="0 0 10 13" aria-hidden="true"><path d="M5 0a5 5 0 0 0-5 5c0 3.5 5 8 5 8s5-4.5 5-8a5 5 0 0 0-5-5z" fill="#fff"/><circle cx="5" cy="5" r="1.8" fill="#111"/></svg>
      <span>5817 Harwick Boulevard West,<br>Scarborough, ON M4R 7K2</span>
    </div>
    <div class="contact-row">
      <svg width="12" height="12" viewBox="0 0 12 12" aria-hidden="true"><path d="M2.5 0.5l2 2.5-1.2 1.5a7 7 0 0 0 4.2 4.2L9 7.5l2.5 2-1.3 2C5 11.5.5 7 .5 1.8z" fill="#fff"/></svg>
      <span>(416) 738-LEAF</span>
    </div>
    <div class="contact-row">
      <svg width="12" height="12" viewBox="0 0 12 12" aria-hidden="true"><circle cx="6" cy="6" r="5" fill="none" stroke="#fff" stroke-width="1.6"/><path d="M6 3v3.3l2 1.2" fill="none" stroke="#fff" stroke-width="1.4"/></svg>
      <span>Hours of Operation<br>Open Daily 10:00 - 10:00</span>
    </div>
  </address>

  <div class="rule abs" style="top:2724px"></div>
  <p class="copyright abs">Copyright © 2021 - Mossfield Cannabis. All Right Reserved</p>

  <a class="to-top abs" href="#" aria-label="Back to top">
    <svg width="22" height="12" viewBox="0 0 22 12" aria-hidden="true"><path d="M1 11 11 1l10 10" fill="none" stroke="#222" stroke-width="1.4"/></svg>
  </a>
</div>
</body>
</html>
```